Global social media analytics company needs business card design

We need an updated business card design to align with our new website - plumvantix.com -

I would also like a favicon designed as well.

Target Market(s)

CEOs, CMOs go big companies

Industry/Entity Type

Business

Contact Information for Business Card

Room for the following:
Address
Main telephone
Direct telephone or cell phone
twitter handle

Colors
aaaaaa

Requirements
Must have
• Attention to detail; style.
• Use the logo color from our website - which is gray

```html
<!DOCTYPE html>
<html lang="en">
<head>
<meta charset="utf-8">
<title>Plumvantix Business Card</title>
<link rel="stylesheet" href="https://fonts.googleapis.com/css2?family=Source+Sans+3:wght@400;600;700&display=swap">
<style>
  :root {
    --backdrop: #404042;
    --card-white: #ffffff;
    --gray-light: #c0c0c0;
    --gray-mid: #a9a9a9;
    --gray-low: #878787;
    --band-top: #5c5e5e;
    --band-bottom: #202222;
    --text-gray: #666666;
    --text-dark: #3f3f3f;
    --mark-gray: #5a5a5a;
  }
  * { margin: 0; padding: 0; box-sizing: border-box; }
  html, body { width: 1200px; height: 900px; overflow: hidden; }
  body {
    background: var(--backdrop);
    font-family: "Source Sans 3", "Myriad Pro", sans-serif;
    position: relative;
  }
  .card {
    position: absolute;
    overflow: hidden;
    box-shadow: 0 3px 6px rgba(0,0,0,0.45);
  }
  .card svg.card-shapes { position: absolute; inset: 0; }
  .card-front { left: 351px; top: 158px; width: 461px; height: 278px; }
  .card-back { left: 351px; top: 480px; width: 462px; height: 277px; background: var(--card-white); }

  .brand {
    position: absolute;
    display: flex;
    align-items: center;
    color: var(--mark-gray);
    font-weight: 700;
    letter-spacing: -0.3px;
  }
  .brand-dot { border-radius: 50%; background: var(--mark-gray); }
  .card-front .brand { right: 37px; top: 47px; font-size: 15px; gap: 6px; }
  .card-front .brand-dot { width: 36px; height: 36px; }
  .card-back .brand { left: 65px; top: 100px; font-size: 27px; gap: 9px; }
  .card-back .brand-dot { width: 60px; height: 60px; }

  .contact {
    position: absolute;
    right: 33px;
    top: 142px;
    text-align: right;
    color: var(--text-gray);
    font-size: 12px;
    line-height: 15px;
    letter-spacing: 0.2px;
  }
  .contact .name { font-weight: 700; font-size: 13px; }
  .contact .title { font-weight: 600; color: var(--card-white); }
  .contact .label { font-weight: 600; }
  .contact .gap { height: 15px; }

  .web-address {
    position: absolute;
    left: 0; width: 406px;
    top: 248px;
    text-align: center;
    font-size: 11px;
    letter-spacing: 2.6px;
    color: var(--text-dark);
  }
</style>
</head>
<body>
  <section class="card card-front">
    <svg class="card-shapes" width="461" height="278" viewBox="0 0 461 278">
      <defs>
        <linearGradient id="frontFace" x1="0" y1="0" x2="0" y2="1">
          <stop offset="0" stop-color="var(--gray-light)"/>
          <stop offset="0.55" stop-color="var(--gray-mid)"/>
          <stop offset="1" stop-color="var(--gray-low)"/>
        </linearGradient>
        <linearGradient id="frontBand" x1="0" y1="0" x2="0" y2="1">
          <stop offset="0" stop-color="var(--band-top)"/>
          <stop offset="0.35" stop-color="#545656"/>
          <stop offset="0.65" stop-color="#2e3030"/>
          <stop offset="1" stop-color="var(--band-bottom)"/>
        </linearGradient>
      </defs>
      <rect width="461" height="278" fill="url(#frontFace)"/>
      <path d="M0 0 H71 Q56 140 79 278 H0 Z" fill="url(#frontBand)"/>
      <path d="M73 0 Q58 140 81 278" fill="none" stroke="var(--card-white)" stroke-width="4"/>
    </svg>
    <div class="brand"><span class="brand-dot"></span>plumvantix</div>
    <div class="contact">
      <div class="name">Daniel Marsh</div>
      <div class="title">Managing Director</div>
      <div>d.marsh@plumvantix.com</div>
      <div class="gap"></div>
      <div><span class="label">Tel:</span> 1 555 014 2290</div>
      <div><span class="label">Mobile:</span> 0555 019 247</div>
      <div>48 Harbor Lane, Suite 2</div>
    </div>
  </section>

  <section class="card card-back">
    <svg class="card-shapes" width="462" height="277" viewBox="0 0 462 277">
      <defs>
        <linearGradient id="backFace" x1="0" y1="0" x2="0" y2="1">
          <stop offset="0" stop-color="var(--gray-light)"/>
          <stop offset="0.6" stop-color="var(--gray-mid)"/>
          <stop offset="1" stop-color="var(--gray-low)"/>
        </linearGradient>
        <linearGradient id="backBand" x1="0" y1="0" x2="0" y2="1">
          <stop offset="0" stop-color="#5e6060"/>
          <stop offset="1" stop-color="var(--band-bottom)"/>
        </linearGradient>
      </defs>
      <path d="M425 0 Q366 140 371 277 H462 V0 Z" fill="url(#backBand)"/>
      <path d="M433 0 Q378 140 386 277 H462 V0 Z" fill="#7a7c7c"/>
      <path d="M437 0 Q384 140 393 277 H462 V0 Z" fill="url(#backFace)"/>
    </svg>
    <div class="brand"><span class="brand-dot"></span>plumvantix</div>
    <div class="web-address">www.plumvantix.com</div>
  </section>
</body>
</html>
```